We invest in Electric Vehicles and renewable energy - help sell us!

INTRO: We want a PowerPoint template / Master Presentation to be used to sell our company and first investment fund to professional investors and to present ourselves to businesses that will develop the infrastructure projects in which we will invest.

WHO WE ARE: We are a newly created investment advisory and fund management company specialised in sustainable mobility.

WHAT WE DO: We invest in infrastructure projects that provide electric vehicles, charging infrastructure (charging stations etc) and associated renewable energy generation services (eg solar panels on roof-tops and solar parks, wind energy). The users of the projects in which we invest are operators of vehicle fleets (taxis, buses, delivery, which may be for 2, 3 and 4 wheel vehicles from motorbikes through cars, vans, buses and trucks).

PURPOSE OF THE POWERPOINT: We are looking for a presentation (1) to sell our investment services to investors (to raise money) and (2) to present what we do to fleet operators and service providers who will develop the projects.

CONTENT: We need all of the usual front cover slide / content slide / intermediate divider-heading slide / slides that integrate the most common tables, charts and smart graphics / team slide / a variety of text slides / a testimonial slide / Example project slide / Final contact and Disclaimer text slide etc all customised to the design. We rely on your experience for providing the further standard formats and layouts that one might find in a high-quality financial sector corporate presentation deck.

VERSIONS: We want three versions of the slides where there are images (eg front and back covers, section breaks, testimonial slides..). The three could be themed eg (1) futuristic and/or abstract in the theme of our investment scope (2) Street themes with vehicles and people in developed and developing markets (3) a mix of aerial and land-based views of roads (4) more explicit around the types of infrastructure in which we invest (vehicles of different types, charging infrastructure, solar panels on industrial and commercial roof tops etc)

LOOK & FEEL: The presentation must be sleek, dynamic if sober, with a clean feel, it should project an image of clarity and confidence, but also elicit some emotional appeal (even if it is very subtle!) ... we are in the e-mobility sector after all! We have an existing logo (attached).

We have an existing website www.quorlane.capital (one day it will need an upgrade too!) it may serve as inspiration / allow you better to understand our activities!

SOME PICS THAT WE LIKE: for inspiration only (NON exhaustive!):

• https://www.frametidepool.com/video/stock/unrecognizable-highway-traffic-head-on-kdwpqzrmtxa42ufhe
• https://www.frametidepool.com/video/stock/new-york-city-streets-qw8mxr5
• https://www.frametidepool.com/video/stock/4k-time-lapse-of-traffic-speeding-on-a-straight-section-of-highway-during-an-evening-rush-hour-zk7wqe3
• https://www.frametidepool.com/video/stock/cinematic-urban-aerial-time-lapse-of-city-infrastructure-including-freeways-interstates-roads-streets-with-traffic-at-rush-hour-during-the-evening-mxtrwpkudzlcfqe4k
• https://www.frametidepool.com/video/stock/charging-of-electric-car-eco-energy-transport-and-power-supply-environmentally-conscious-transportation-vehicle-plugged-in-charger-terminal-in-the-city-4k-wvt3hdyxnacbzkfmee
• https://www.frametidepool.com/video/stock/drone-view-of-modern-vehicle-driving-on-road-near-ploughed-field-and-wind-turbine-in-countryside-hpxmbwtlcjr27nqeu

FINALLY: note the attached 'slides to include' are additonal slides that we want to be well presented (see additional detail on Slide 1 of the file)

Institutional investors (pension funds, asset managers, family offices) & the dreamer in each of us!!

Financial services (B2B NOT B2C)

• Calibri but can consider alternatives

• We need all of the usual front cover slide / content slide / intermediate divider-heading slide / slides that integrate the most common tables, charts and smart graphics / team slide / a variety of text slides / a testimonial slide / Example project slide / Final contact and Disclaimer text slide etc all customised to the design. We rely on your experience for providing the further standard formats and layouts that one might find in a high-quality financial sector corporate presentation deck
• Would like to see any other pages that are standard in your experience! Also would like to see one version of the slides with a summary section clearly marked for each slide (with space for text) which will serve for quick reading of the presentation for key points)

```html
<!DOCTYPE html>
<html lang="en">
<head>
<meta charset="utf-8">
<title>Quorlane Capital – Presentation Slides</title>
<link href="https://fonts.googleapis.com/css2?family=Roboto:wght@300;400;500;700&display=swap" rel="stylesheet">
<style>
:root{
  --green-dark:#3b5a1c;
  --green:#4f7a26;
  --green-mid:#6f9a3a;
  --green-light:#8fd14f;
  --green-bright:#5fe05a;
  --ink:#333;
  --muted:#8a8a8a;
  --line:#d6d6d6;
  --accent:#e0863a;
  --paper:#ffffff;
}
*{margin:0;padding:0;box-sizing:border-box}
html,body{width:815px;height:1200px;overflow:hidden;background:var(--paper);font-family:"Roboto",Arial,sans-serif;color:var(--ink)}
.canvas{position:relative;width:815px;height:1200px}
.slide{position:absolute;width:303px;height:171px;background:var(--paper);overflow:hidden;box-shadow:0 5px 14px rgba(0,0,0,.2)}
.col-l{left:72px}.col-r{left:437px}
.r1{top:29px}.r2{top:223px}.r3{top:417px}.r4{top:611px}.r5{top:804px}.r6{top:998px}
.abs{position:absolute}
.brand{position:absolute;top:13px;right:29px;font-size:6px;font-weight:500;color:var(--green-dark);letter-spacing:.1px}
.brand.light{color:#fff}
.title{position:absolute;font-size:12px;font-weight:300;color:var(--green-dark);white-space:nowrap}
.title b{font-weight:700}
.subtitle{position:absolute;font-size:4.6px;letter-spacing:.9px;color:#444}
.para{position:absolute;font-size:3.2px;line-height:1.68;color:var(--muted);text-align:justify}
.bullets{position:absolute;font-size:3.2px;line-height:1.7;color:var(--muted);text-align:justify;padding-left:7px}
.bullets li{margin-bottom:2.6px}
.foot{position:absolute;bottom:6px;left:23px;font-size:3.4px;color:#aaa}
.pg{position:absolute;bottom:6px;right:24px;font-size:3.4px;color:#aaa}
.photo{position:absolute}
.svc-icon{position:absolute;width:20px;height:20px;border-radius:50%;background:var(--green-dark)}
.svc-name{position:absolute;font-size:3.4px;font-weight:700;color:var(--green-dark);white-space:nowrap}
.svc-text{position:absolute;font-size:2.6px;line-height:1.6;color:var(--muted);width:48px}
.col-head{position:absolute;font-size:4.4px;font-weight:700;color:var(--green-dark)}
.tl-year{position:absolute;font-size:5px;color:#666;line-height:1.1}
.tl-year span{display:block;color:var(--green-dark);font-size:4.6px}
.tl-year small{display:block;font-size:2.4px;color:var(--green-mid);width:32px;line-height:1.3}
.q-dot{position:absolute;width:12px;height:12px;border-radius:50%}
.q-name{position:absolute;font-size:4px;font-weight:500;color:var(--green-dark)}
.q-text{position:absolute;font-size:2.6px;line-height:1.6;color:var(--muted);width:38px}
.item-dot{position:absolute;width:14px;height:14px;border-radius:50%;background:var(--green-dark)}
.item-title{position:absolute;font-size:3.4px;font-weight:700;color:var(--green-dark)}
.item-text{position:absolute;font-size:2.6px;line-height:1.6;color:var(--muted);width:42px}
.cover-name{position:absolute;font-size:17px;font-weight:400;color:#fff}
.cover-sub{position:absolute;font-size:11px;font-weight:300;color:#fff}
.cover-sub b{font-weight:700}
</style>
</head>
<body>
<div class="canvas">

<!-- Our Vision -->
<section class="slide col-l r1">
  <div class="brand">Quorlane Capital</div>
  <h2 class="title" style="left:21px;top:24px">Our <b>Vision</b></h2>
  <div class="subtitle" style="left:21px;top:44px">Subtitle Text</div>
  <ul class="bullets" style="left:22px;top:56px;width:133px">
    <li>Lorem Ipsum is simply dummy text of the printing and typesetting industry. Lorem Ipsum has been the industry's standard dummy text ever since the 1500s, when an unknown printer took a galley of type and scrambled it to</li>
    <li>Make a type specimen book. It has survived not only five centuries, but also the leap into electronic typesetting, remaining essentially unchanged. It was popularized in the 1960s with the release of</li>
    <li>Letraset sheets containing Lorem Ipsum passages, and more recently with desktop publishing software like Aldus PageMaker including versions of Lorem Ipsum.</li>
    <li>It is a long established fact that a reader will be distracted by the readable content of a page when looking at its layout. The point of using Lorem Ipsum is that it has a more-or-less normal distribution of letters</li>
  </ul>
  <div class="photo" role="img" aria-label="Electric vehicle charging station under a canopy" style="left:171px;top:24px;width:132px;height:123px;background:linear-gradient(170deg,#e8e4c2 0%,#c9c48a 35%,#7fa08f 65%,#3f8a78 100%)"></div>
  <div class="foot">quorlane.capital</div><div class="pg">13</div>
</section>

<!-- Our Services (photo band) -->
<section class="slide col-r r1">
  <div class="brand">Quorlane Capital</div>
  <h2 class="title" style="left:22px;top:16px">Our <b>Services</b></h2>
  <div class="subtitle" style="left:21px;top:34px">Subtitle Text</div>
  <p class="para" style="left:22px;top:44px;width:259px">Lorem Ipsum is simply dummy text of the printing and typesetting industry. Lorem Ipsum has been the industry's standard dummy text ever since the 1500s, when an unknown printer took a galley of type and scrambled it to Make a type specimen book. It has survived not only five centuries, but also the leap into electronic typesetting, remaining essentially unchanged. It was popularised in the 1960s with the release of Letraset sheets containing Lorem Ipsum passages, and more recently with desktop publishing software like Aldus PageMaker including versions of Lorem Ipsum. It is a long established fact that a reader will be distracted by the readable content of a page when looking at its layout. The point of using Lorem Ipsum is that it has a more-or-less normal</p>
  <div class="photo" role="img" aria-label="Zero emission electric bus driving past trees" style="left:0;top:85px;width:303px;height:86px;background:linear-gradient(90deg,#4f7a35 0%,#c9ced0 25%,#e9ecee 55%,#7f9a6a 85%,#5c7f3f 100%)"></div>
</section>

<!-- Our Services (icons) -->
<section class="slide col-l r2">
  <div class="brand">Quorlane Capital</div>
  <h2 class="title" style="left:22px;top:17px">Our <b>Services</b></h2>
  <div class="subtitle" style="left:21px;top:36px">Subtitle Text</div>
  <p class="para" style="left:22px;top:47px;width:259px">Lorem Ipsum is simply dummy text of the printing and typesetting industry. Lorem Ipsum has been the industry's standard dummy text ever since the 1500s, when an unknown printer took a galley of type and scrambled it to Make a type specimen book. It has survived not only five centuries, but also the leap into electronic typesetting, remaining essentially unchanged. It was popularized in the 1960s with the release of Letraset sheets containing Lorem Ipsum passages, and more recently with desktop publishing software like Aldus PageMaker including versions of Lorem Ipsum. It is a long established fact that a reader will be distracted by the readable content of a page when looking at its layout. The point of using Lorem Ipsum is that it has a more-or-less normal</p>
  <div class="svc-icon" style="left:22px;top:93px"></div>
  <div class="svc-name" style="left:48px;top:94px">Service, Repair &amp; After Service</div>
  <div class="svc-text" style="left:48px;top:99px">Mattis pellentesque id nibh tortor id aliquet. Libero id faucibus nisl</div>
  <div class="svc-icon" style="left:111px;top:93px"></div>
  <div class="svc-name" style="left:137px;top:94px">Training</div>
  <div class="svc-text" style="left:137px;top:99px">Mattis pellentesque id nibh tortor id aliquet. Libero id faucibus nisl</div>
  <div class="svc-icon" style="left:200px;top:93px"></div>
  <div class="svc-name" style="left:226px;top:94px">Logistic &amp; Delivery</div>
  <div class="svc-text" style="left:226px;top:99px">Mattis pellentesque id nibh tortor id aliquet. Libero id faucibus nisl</div>
  <div class="svc-icon" style="left:22px;top:127px"></div>
  <div class="svc-name" style="left:48px;top:128px">Operational Streamlining</div>
  <div class="svc-text" style="left:48px;top:133px">Mattis pellentesque id nibh tortor id aliquet. Libero id faucibus nisl</div>
  <div class="svc-icon" style="left:111px;top:127px"></div>
  <div class="svc-name" style="left:137px;top:128px">Team Expert</div>
  <div class="svc-text" style="left:137px;top:133px">Mattis pellentesque id nibh tortor id aliquet. Libero id faucibus nisl</div>
  <div class="svc-icon" style="left:200px;top:127px"></div>
  <div class="svc-name" style="left:226px;top:128px">Account Management</div>
  <div class="svc-text" style="left:226px;top:133px">Mattis pellentesque id nibh tortor id aliquet. Libero id faucibus nisl</div>
  <svg class="abs" style="left:0;top:0" width="303" height="171" fill="none" stroke="#fff" stroke-width=".7" aria-hidden="true">
    <path d="M28 99l8 8M36 99l-8 8"/><rect x="116" y="98" width="10" height="7"/><path d="M207 98h5v10h-5zM212 104h3v4"/>
    <rect x="27" y="132" width="10" height="10"/><circle cx="118" cy="135" r="1.5"/><circle cx="124" cy="135" r="1.5"/><path d="M115 142v-3h12v3"/><circle cx="210" cy="134" r="2"/><path d="M206 143v-4h8v4"/>
  </svg>
  <div class="foot">quorlane.capital</div><div class="pg">16</div>
</section>

<!-- Our Services (photo grid) -->
<section class="slide col-r r2">
  <div class="brand">Quorlane Capital</div>
  <div class="photo" role="img" aria-label="Car exhaust in city traffic" style="left:22px;top:28px;width:63px;height:58px;background:linear-gradient(160deg,#6a6e72,#b9bcbf 60%,#8a5a4a)"></div>
  <div class="photo" role="img" aria-label="Truck on a road at night" style="left:86px;top:28px;width:63px;height:58px;background:linear-gradient(160deg,#2f3a3c,#5c6e6a 60%,#232a2b)"></div>
  <div class="photo" role="img" aria-label="Highway traffic seen from a car" style="left:22px;top:87px;width:63px;height:58px;background:linear-gradient(180deg,#9aa49c,#6b7a6a 60%,#3f4a42)"></div>
  <div class="photo" role="img" aria-label="Yellow taxis on a city street" style="left:86px;top:87px;width:63px;height:58px;background:linear-gradient(160deg,#8b8f86,#5d6460 50%,#c9a12b)"></div>
  <h2 class="title" style="left:162px;top:22px">Our <b>Services</b></h2>
  <ul class="bullets" style="left:162px;top:43px;width:121px">
    <li>Lorem Ipsum is simply dummy text of the printing and typesetting industry. Lorem Ipsum has been the industry's standard dummy text ever since the 1500s, when an unknown printer took a galley of type and scrambled it to</li>
    <li>Make a type specimen book. It has survived not only five centuries, but also the leap into electronic typesetting, remaining essentially unchanged. It was popularized in the 1960s with the release of</li>
    <li>Letraset sheets containing Lorem Ipsum passages, and more recently with desktop publishing software like Aldus PageMaker including versions of Lorem Ipsum.</li>
    <li>It is a long established fact that a reader will be distracted by the readable content of a page when looking at its layout. The point of using Lorem Ipsum is that it has a more-or-less normal distribution of letters, as opposed to using</li>
  </ul>
  <div class="foot">quorlane.capital</div><div class="pg">15</div>
</section>

<!-- Business Strategy -->
<section class="slide col-l r3">
  <div class="brand">Quorlane Capital</div>
  <h2 class="title" style="left:22px;top:19px">Business <b>Strategy</b></h2>
  <div class="subtitle" style="left:22px;top:38px">Subtitle Text</div>
  <p class="para" style="left:22px;top:48px;width:259px">Lorem Ipsum is simply dummy text of the printing and typesetting industry. Lorem Ipsum has been the industry's standard dummy text ever since the 1500s, when an unknown printer took a galley of type and scrambled it to Make a type specimen book. It has survived not only five centuries, but also the leap into electronic typesetting, remaining essentially unchanged. It was popularized in the 1960s with the release of Letraset sheets containing Lorem Ipsum passages, and more recently with desktop publishing software like Aldus PageMaker including versions of Lorem Ipsum. It is a long established fact that a</p>
  <svg class="abs" style="left:0;top:0" width="303" height="171" fill="none" stroke="#3b5a1c" stroke-width=".7" aria-hidden="true">
    <rect x="23" y="83" width="12" height="8"/><path d="M25 89l3-3 2 2 3-3M29 91v3M26 94h6"/>
    <circle cx="120" cy="85" r="3"/><path d="M114 95c0-4 3-6 6-6s6 2 6 6z"/>
    <circle cx="211" cy="85" r="3"/><path d="M205 95c0-4 3-6 6-6M216 91l1 2 2 .3-1.5 1.4.4 2-1.9-1-1.9 1 .4-2-1.5-1.4 2-.3z"/>
  </svg>
  <div class="col-head" style="left:22px;top:103px">Innovative Business Practice:</div>
  <div class="col-head" style="left:114px;top:103px">Customer Support:</div>
  <div class="col-head" style="left:206px;top:103px">Knowledge Support:</div>
  <ul class="bullets" style="left:22px;top:113px;width:78px"><li>Orci a scelerisque purus semper eget duis at. Enim facilisis gravida neque convallis. Amet consectetur adipiscing elit pellentesque.</li><li>In metus vulputate eu scelerisque felis imperdiet proin. Velit ut tortor pretium viverra suspendisse potenti nullam ac tortor.</li></ul>
  <ul class="bullets" style="left:114px;top:113px;width:78px"><li>Orci a scelerisque purus semper eget duis at. Enim facilisis gravida neque convallis. Amet consectetur adipiscing elit pellentesque.</li><li>Scelerisque mauris pellentesque pulvinar pellentesque habitant morbi tristique senectus et. Cras semper auctor neque vitae.</li></ul>
  <ul class="bullets" style="left:206px;top:113px;width:78px"><li>Orci a scelerisque purus semper eget duis at. Enim facilisis gravida neque convallis. Amet consectetur adipiscing elit pellentesque.</li><li>Scelerisque mauris pellentesque pulvinar pellentesque habitant morbi tristique senectus et. Cras semper auctor neque vitae.</li></ul>
  <div class="foot">quorlane.capital</div><div class="pg">18</div>
</section>

<!-- Our Strengths -->
<section class="slide col-r r3">
  <h2 class="title" style="left:22px;top:17px;font-size:17px">Our <b>Strengths</b></h2>
  <ul class="bullets" style="left:22px;top:46px;width:133px">
    <li>Lorem Ipsum is simply dummy text of the printing and typesetting industry. Lorem Ipsum has been the industry's standard dummy text ever since the 1500s, when an unknown printer took a galley of type and scrambled it to</li>
    <li>Make a type specimen book. It has survived not only five centuries, but also the leap into electronic typesetting, remaining essentially unchanged. It was popularized in the 1960s with the release of</li>
    <li>Letraset sheets containing Lorem Ipsum passages, and more recently with desktop publishing software like Aldus PageMaker including versions of Lorem Ipsum.</li>
    <li>It is a long established fact that a reader will be distracted by the readable content of a page when looking at its layout. The point of using Lorem Ipsum is that it has a more-or-less normal distribution of letters, as opposed to using</li>
  </ul>
  <div class="photo" role="img" aria-label="Charging plug connected to an electric car, green tinted" style="left:171px;top:0;width:132px;height:171px;background:linear-gradient(135deg,#5f7a4c 0%,#3d5632 45%,#22301d 75%,#4a6338 100%)"></div>
  <div class="brand light">Quorlane Capital</div>
  <div class="foot">quorlane.capital</div>
</section>

<!-- Timeline Operations -->
<section class="slide col-l r4">
  <div class="brand">Quorlane Capital</div>
  <h2 class="title" style="left:22px;top:18px">Timeline <b>Operations</b></h2>
  <div class="subtitle" style="left:22px;top:37px">Subtitle Text</div>
  <div class="tl-year" style="left:55px;top:48px">2012<span>Lorem Ipsum</span><small>is simply dummy text of the printing and typesetting</small></div>
  <div class="tl-year" style="left:120px;top:48px">2016<span>Lorem Ipsum</span><small>is simply dummy text of the printing and typesetting</small></div>
  <div class="tl-year" style="left:186px;top:48px">2019<span>Lorem Ipsum</span><small>is simply dummy text of the printing and typesetting</small></div>
  <div class="tl-year" style="left:251px;top:48px">2021<span>Lorem Ipsum</span><small>is simply dummy text of the printing and typesetting</small></div>
  <div class="tl-year" style="left:23px;top:115px">2010<span>Lorem Ipsum</span><small>is simply dummy text of the printing and typesetting</small></div>
  <div class="tl-year" style="left:88px;top:115px">2014<span>Lorem Ipsum</span><small>is simply dummy text of the printing and typesetting</small></div>
  <div class="tl-year" style="left:154px;top:115px">2018<span>Lorem Ipsum</span><small>is simply dummy text of the printing and typesetting</small></div>
  <div class="tl-year" style="left:219px;top:115px">2020<span>Lorem Ipsum</span><small>is simply dummy text of the printing and typesetting</small></div>
  <svg class="abs" style="left:0;top:0" width="303" height="171" fill="none" aria-hidden="true">
    <g stroke="#cfcfcf" stroke-width=".5">
      <path d="M55 76h32M55 76v5M120 76h32M120 76v5M186 76h32M186 76v5M251 76h32M251 76v5"/>
      <path d="M23 111h32M23 111v-5M88 111h32M88 111v-5M154 111h32M154 111v-5M219 111h32M219 111v-5"/>
    </g>
    <g stroke="#3b5a1c" stroke-width=".6">
      <rect x="24" y="88" width="16" height="11"/><path d="M27 88v-3h10v3"/>
      <rect x="56" y="88" width="16" height="11"/><path d="M61 88v-2h6v2M56 93h16"/>
      <rect x="90" y="84" width="14" height="14"/><path d="M93 88h8M93 91h8M93 94h6"/>
      <path d="M122 96l5-5 3 3 5-5M123 86l4 3M133 86l-4 3"/>
      <rect x="154" y="88" width="14" height="10"/><path d="M154 93h14M161 88v10M161 82v3M157 84l1 2M165 84l-1 2"/>
      <path d="M190 99V87M190 87l-5-3M190 87l5-3M190 87v-5M200 99v-9M200 90l-3-2M200 90l3-2"/>
      <path d="M224 99v-8M220 86h8v5h-8zM222 86v-3M226 86v-3M229 96c3-5 6-5 8-7-1 4-3 7-8 7z"/>
      <path d="M252 99v-10l4-3v13M256 99v-8l4-3v11M260 99V84h4v15zM250 99h16"/>
    </g>
  </svg>
  <div class="foot">quorlane.capital</div><div class="pg">20</div>
</section>

<!-- Our Operations -->
<section class="slide col-r r4">
  <div class="brand">Quorlane Capital</div>
  <h2 class="title" style="left:22px;top:18px">Our <b>Operations</b></h2>
  <div class="subtitle" style="left:22px;top:37px">Subtitle Text</div>
  <svg class="abs" style="left:0;top:0" width="303" height="171" fill="none" stroke="#aaa" stroke-width=".4" stroke-dasharray="1 1" aria-hidden="true">
    <path d="M29 63v-10h66v10M95 63v10h66v-10M161 63v-10h66v10"/>
    <path d="M29 101v-10h66v10M95 101v-10h66v10M161 101v-10h66v10"/>
  </svg>
  <div class="q-dot" style="left:23px;top:57px;background:var(--green-dark)"></div>
  <div class="q-dot" style="left:89px;top:57px;background:#2e4a16"></div>
  <div class="q-dot" style="left:155px;top:57px;background:#5b7a48"></div>
  <div class="q-dot" style="left:221px;top:57px;background:#7fbf4a"></div>
  <div class="q-dot" style="left:23px;top:95px;background:#5b7a3a"></div>
  <div class="q-dot" style="left:89px;top:95px;background:#4b7a34"></div>
  <div class="q-dot" style="left:155px;top:95px;background:#a3c21a"></div>
  <div class="q-dot" style="left:221px;top:95px;background:#21b53a"></div>
  <div class="q-name" style="left:41px;top:56px">Q1a</div><div class="q-text" style="left:41px;top:62px">Mattis pellentesque id nibh tortor id aliquet. Libero id faucibus nisl tincidunt eget.</div>
  <div class="q-name" style="left:107px;top:46px">Q2a</div><div class="q-text" style="left:107px;top:52px">Mattis pellentesque id nibh tortor id aliquet. Libero id faucibus nisl tincidunt eget.</div>
  <div class="q-name" style="left:173px;top:56px">Q3a</div><div class="q-text" style="left:173px;top:62px">Mattis pellentesque id nibh tortor id aliquet. Libero id faucibus nisl tincidunt eget.</div>
  <div class="q-name" style="left:239px;top:46px">Q4a</div><div class="q-text" style="left:239px;top:52px">Mattis pellentesque id nibh tortor id aliquet. Libero id faucibus nisl tincidunt eget.</div>
  <div class="q-name" style="left:41px;top:84px">Q4b</div><div class="q-text" style="left:41px;top:90px">Mattis pellentesque id nibh tortor id aliquet. Libero id faucibus nisl tincidunt eget.</div>
  <div class="q-name" style="left:107px;top:94px">Q3b</div><div class="q-text" style="left:107px;top:100px">Mattis pellentesque id nibh tortor id aliquet. Libero id faucibus nisl tincidunt eget.</div>
  <div class="q-name" style="left:173px;top:84px">Q2b</div><div class="q-text" style="left:173px;top:90px">Mattis pellentesque id nibh tortor id aliquet. Libero id faucibus nisl tincidunt eget.</div>
  <div class="q-name" style="left:239px;top:94px">Q1b</div><div class="q-text" style="left:239px;top:100px">Mattis pellentesque id nibh tortor id aliquet. Libero id faucibus nisl tincidunt eget.</div>
  <p class="para" style="left:22px;top:125px;width:259px">Orci a scelerisque purus semper eget duis at. Enim facilisis gravida neque convallis. Amet consectetur adipiscing elit pellentesque. Ut placerat orci nulla pellentesque dignissim enim sit amet. Urna neque viverra justo nec. Pellentesque id nibh tortor id aliquet. Est pellentesque elit ullamcorper dignissim cras tincidunt lobortis feugiat vivamus. Scelerisque mauris pellentesque pulvinar pellentesque habitant morbi tristique senectus et. Ac turpis egestas sed tempus urna. Sit amet massa vitae tortor condimentum lacinia quis vel eros. Quis vel eros donec ac odio. Dolor magna eget est lorem ipsum dolor sit.</p>
  <div class="foot">quorlane.capital</div><div class="pg">19</div>
</section>

<!-- Company Operations -->
<section class="slide col-l r5">
  <div class="brand">Quorlane Capital</div>
  <svg class="photo" style="left:22px;top:26px" width="260" height="122" role="img" aria-label="Hydrogen powered city bus on a road beside trees">
    <defs><linearGradient id="busTone" x1="0" y1="0" x2="1" y2="1"><stop offset="0" stop-color="#4d7a32"/><stop offset=".45" stop-color="#c8d0d4"/><stop offset=".75" stop-color="#e6eaec"/><stop offset="1" stop-color="#6f8a4e"/></linearGradient></defs>
    <path d="M0 0H63V61H260V122H0z" fill="url(#busTone)"/>
  </svg>
  <h2 class="title" style="left:99px;top:27px">Company <b>Operations</b></h2>
  <p class="para" style="left:99px;top:51px;width:183px">Lorem Ipsum is simply dummy text of the printing and typesetting industry. Lorem Ipsum has been the industry's standard dummy text ever since the 1500s, when an unknown printer took a galley of type and scrambled it to Make a type specimen book. It has survived not only five centuries, but also the leap into electronic typesetting, remaining essentially unchanged. It was popularized in the 1960s with the release of</p>
  <div class="foot">quorlane.capital</div><div class="pg">21</div>
</section>

<!-- Company Marketing cover -->
<section class="slide col-r r5">
  <div class="photo" role="img" aria-label="Charging station canopy with a strong green overlay" style="left:0;top:0;width:303px;height:171px;background:linear-gradient(160deg,#b6c46a 0%,#9cb35a 35%,#7a9c4a 65%,#5e853c 100%)"></div>
  <div class="cover-name" style="left:31px;top:110px">Quorlane Capital</div>
  <div class="cover-sub" style="left:31px;top:137px">Company <b>Marketing</b></div>
</section>

<!-- Your title slide here -->
<section class="slide col-l r6">
  <div class="brand">Quorlane Capital</div>
  <h2 class="title" style="left:98px;top:11px">Your title <b>slide here</b></h2>
  <div class="subtitle" style="left:133px;top:31px">Subtitle Text</div>
  <p class="para" style="left:22px;top:46px;width:46px;text-align:left">Lorem Ipsum is simply dummy text of the printing and typesetting industry. Lorem Ipsum has been the industry's standard dummy text ever since the 1500s, when an unknown printer took a galley of type and scrambled it to Make a type specimen book. It has survived not only five centuries, but also the leap into electronic typesetting, remaining essentially</p>
  <svg class="abs" style="left:66px;top:43px" width="160" height="100" aria-hidden="true">
    <rect x="14" y="1" width="134" height="89" rx="4" fill="#2a2a2a"/>
    <path d="M0 91h160l-6 4H6z" fill="#c9c9c9"/>
  </svg>
  <div class="photo" role="img" aria-label="Silhouettes of two people under solar panels at sunset" style="left:83px;top:47px;width:126px;height:80px;background:linear-gradient(180deg,#1b2a4a 0%,#3a4a7a 40%,#c27a3a 75%,#1a1a22 100%)"></div>
  <div class="item-dot" style="left:227px;top:50px"></div><div class="item-title" style="left:246px;top:50px">Your Title</div><div class="item-text" style="left:246px;top:55px">Mattis pellentesque id nibh tortor id aliquet. Libero id faucibus nisl</div>
  <div class="item-dot" style="left:227px;top:72px"></div><div class="item-title" style="left:246px;top:72px">Your Title</div><div class="item-text" style="left:246px;top:77px">Mattis pellentesque id nibh tortor id aliquet. Libero id faucibus nisl</div>
  <div class="item-dot" style="left:227px;top:94px"></div><div class="item-title" style="left:246px;top:94px">Your Title</div><div class="item-text" style="left:246px;top:99px">Mattis pellentesque id nibh tortor id aliquet. Libero id faucibus nisl</div>
  <div class="item-dot" style="left:227px;top:116px"></div><div class="item-title" style="left:246px;top:116px">Your Title</div><div class="item-text" style="left:246px;top:121px">Mattis pellentesque id nibh tortor id aliquet. Libero id faucibus nisl</div>
  <div class="foot">quorlane.capital</div><div class="pg">23</div>
</section>

<!-- Target Market -->
<section class="slide col-r r6">
  <div class="brand">Quorlane Capital</div>
  <svg class="abs" style="left:14px;top:36px" width="150" height="110" font-family="Roboto, sans-serif" font-size="3.4" fill="#888" role="img" aria-label="Bar chart of monthly values from February to May">
    <g text-anchor="end"><text x="6" y="2">70</text><text x="6" y="14">60</text><text x="6" y="25.5">50</text><text x="6" y="37">40</text><text x="6" y="48.5">30</text><text x="6" y="60">20</text><text x="6" y="71.5">10</text><text x="6" y="83">0</text></g>
    <g>
      <rect x="10" y="72" width="5" height="10" fill="#3b5a1c"/><rect x="16" y="53" width="5" height="29" fill="#6f9a3a"/><rect x="22" y="52" width="5" height="30" fill="#5fe05a"/><rect x="28" y="34" width="5" height="48" fill="#2e4a16"/>
      <rect x="43" y="71" width="5" height="11" fill="#3b5a1c"/><rect x="49" y="25" width="5" height="57" fill="#6f9a3a"/><rect x="55" y="54" width="5" height="28" fill="#5fe05a"/><rect x="61" y="11" width="5" height="71" fill="#2e4a16"/>
      <rect x="76" y="38" width="5" height="44" fill="#6f9a3a"/><rect x="82" y="7" width="5" height="75" fill="#2e4a16"/><rect x="88" y="68" width="5" height="14" fill="#5fe05a"/><rect x="94" y="68" width="5" height="14" fill="#6f9a3a"/>
      <rect x="109" y="65" width="5" height="17" fill="#3b5a1c"/><rect x="115" y="57" width="5" height="25" fill="#2e4a16"/><rect x="121" y="73" width="5" height="9" fill="#5fe05a"/><rect x="127" y="67" width="5" height="15" fill="#3b5a1c"/>
    </g>
    <g text-anchor="middle"><text x="24" y="89">Feb</text><text x="57" y="89">Mar</text><text x="90" y="89">Apr</text><text x="123" y="89">May</text></g>
    <text x="75" y="103" text-anchor="middle" fill="#e0863a" font-size="3.2" letter-spacing=".3">Fusce a felis porta, ultrices arcu eu, ultricies magna.</text>
  </svg>
  <h2 class="title" style="left:171px;top:29px">Target <b>Market</b></h2>
  <div class="subtitle" style="left:171px;top:49px">Subtitle Text</div>
  <p class="para" style="left:171px;top:60px;width:110px">Lorem Ipsum is simply dummy text of the printing and typesetting industry. Lorem Ipsum has been the industry's standard dummy text ever since the 1500s, when an unknown printer took a galley of type and scrambled it to Make a type specimen book. It has survived not only five centuries, but also the leap into electronic typesetting, remaining essentially unchanged. It was popularized in the 1960s with the release of Letraset sheets containing Lorem Ipsum passages, and more recently with desktop publishing software like Aldus PageMaker including versions of Lorem Ipsum. It is a long established fact that a</p>
  <div class="foot">quorlane.capital</div><div class="pg">24</div>
</section>

</div>
</body>
</html>
```